Financial Service Company Need Business Card Design

This is a new startup company, first of its kind to offer this service. We facilitate the movement of deposit funds electronically between home buyers and real estate brokerages.Our customers are REALTORS®, real estate brokerages, and home buyers, we identify ourselves as a financial/technology company.
Not looking for anything too flashy. Just a clean design that shows the logo, contact info, etc. Company colors can be seen on attached logo, and 'coming soon page'
www.plumvault.ca
Industry/Entity Type
Business
Contact Information for Business Card

```html
<!DOCTYPE html>
<html lang="en">
<head>
<meta charset="utf-8">
<title>PlumVault – Business Card</title>
<link rel="stylesheet" href="https://fonts.googleapis.com/css2?family=Open+Sans:wght@300;400;600&display=swap">
<style>
  :root {
    --stage: #e6e7e8;
    --paper: #ffffff;
    --ink: #58595b;
    --ink-soft: #6d6e71;
    --band: #58595b;
    --accent: #f15a24;
    --sky: #7cc6e4;
  }
  * { box-sizing: border-box; margin: 0; padding: 0; }
  html, body { width: 1200px; height: 777px; overflow: hidden; }
  body {
    background: var(--stage);
    font-family: "Open Sans", sans-serif;
    color: var(--ink);
    position: relative;
  }
  .card {
    position: absolute;
    top: 230px;
    width: 520px;
    height: 297px;
    background: var(--paper);
    box-shadow: 0 2px 10px rgba(0,0,0,0.12);
    overflow: hidden;
  }
  .card--front { left: 50px; }
  .card--back { left: 630px; }

  /* Brand name stand-in */
  .brand { display: flex; align-items: center; gap: 14px; }
  .brand__square { width: 34px; height: 34px; background: var(--accent); flex: none; }
  .brand__name { font-weight: 600; letter-spacing: -0.5px; line-height: 1; }

  /* Front */
  .card--front .front__inner {
    position: absolute; inset: 0;
    display: flex; flex-direction: column; align-items: center; justify-content: center;
    gap: 18px;
  }
  .card--front .brand__name { font-size: 52px; color: var(--ink); }
  .front__url { font-size: 19px; color: var(--accent); letter-spacing: 0.3px; }

  /* Back */
  .person { position: absolute; left: 30px; top: 28px; }
  .person__name { font-size: 27px; font-weight: 300; letter-spacing: 1px; color: var(--ink); text-transform: uppercase; }
  .person__role { font-size: 13px; color: var(--accent); letter-spacing: 1px; text-transform: uppercase; margin-top: 2px; }

  .band {
    position: absolute; left: 0; right: 0; top: 100px; height: 104px;
    background: var(--band);
    border-bottom: 5px solid var(--sky);
  }
  .band__title {
    position: absolute; right: 24px; top: 8px;
    font-size: 40px; font-weight: 600; color: var(--paper); letter-spacing: -0.5px;
  }
  .band .brand { position: absolute; left: 30px; bottom: 12px; }
  .band .brand__square { width: 26px; height: 26px; }
  .band .brand__name { font-size: 30px; color: var(--paper); }

  .contact { position: absolute; left: 30px; right: 24px; top: 214px; font-size: 12.5px; color: var(--ink-soft); }
  .contact__address { margin-bottom: 10px; }
  .contact__cols { display: flex; align-items: stretch; gap: 22px; }
  .contact__col { display: flex; flex-direction: column; gap: 6px; }
  .contact__divider { width: 1px; background: var(--ink-soft); opacity: 0.6; }
  .contact__line { display: flex; align-items: center; gap: 8px; }
  .badge {
    width: 16px; height: 16px; border-radius: 50%;
    background: var(--accent); color: var(--paper);
    font-size: 9px; font-weight: 600;
    display: inline-flex; align-items: center; justify-content: center; flex: none;
  }
</style>
</head>
<body>

  <section class="card card--front" aria-label="Business card front">
    <div class="front__inner">
      <div class="brand">
        <span class="brand__square"></span>
        <span class="brand__name">PlumVault</span>
      </div>
      <p class="front__url">www.plumvault.ca</p>
    </div>
  </section>

  <section class="card card--back" aria-label="Business card back">
    <div class="person">
      <h1 class="person__name">Marcus Hale</h1>
      <p class="person__role">Founder / Director</p>
    </div>

    <div class="band">
      <span class="band__title">PlumVault</span>
      <div class="brand">
        <span class="brand__square"></span>
        <span class="brand__name">PlumVault</span>
      </div>
    </div>

    <div class="contact">
      <p class="contact__address">418 Cedar Ridge Lane, Alberta, T2K-4R7, CA.</p>
      <div class="contact__cols">
        <div class="contact__col">
          <p class="contact__line"><span class="badge">E</span>hello@plumvault.ca</p>
          <p class="contact__line"><span class="badge">W</span>www.plumvault.ca</p>
        </div>
        <span class="contact__divider"></span>
        <div class="contact__col">
          <p class="contact__line"><span class="badge">P</span>902 555 0147</p>
          <p class="contact__line"><span class="badge">F</span>902 555 0148</p>
        </div>
      </div>
    </div>
  </section>

</body>
</html>
```